Dorans Greens

We require an A4 landscape leaflet with a fold down the middle, designed on all 4 sides to represent our home delivery fruit and vegetable box scheme. The leaflet should emphasize on our Free Trial Box offer (no commitment/obligation / £2 delivery charge applies / contents are 100% free) Offer applies to our small box only. We do a large box for £18.50, a medium box for £13 and a small box for £7.50. The leaflet should also show that we deliver extra products such as milk, artisan bread, meat boxes, fresh fish boxes, award winning sausage/pies etc
For more info on our service visit www.doransgreens.co.uk
Updates

Project Deadline Extended
Reason: Currently away so need more time to decide and apply changes required.

Industry/Entity Type

Landscape

```html
<!DOCTYPE html>
<html lang="en">
<head>
<meta charset="utf-8">
<title>Dorans Greens – Home Delivery Leaflet</title>
<link href="https://fonts.googleapis.com/css2?family=Boogaloo&family=Patua+One&family=Crimson+Pro:wght@400;700&display=swap" rel="stylesheet">
<style>
:root{
  --page:#ececea;
  --wood-green:#9cb68a;
  --wood-green-line:#8aa779;
  --wood-beige:#c9bfa9;
  --wood-beige-line:#b9ae97;
  --yellow:#f3c84a;
  --red:#b2232e;
  --white:#ffffff;
  --cream:#f4ecd2;
  --ink:#3f3a30;
  --logo-green:#4e7a2c;
  --tab-dash:#c9c9c9;
}
*{box-sizing:border-box;margin:0;padding:0}
html,body{width:788px;height:1200px;overflow:hidden;background:var(--page)}
body{font-family:"Crimson Pro",Georgia,serif;color:var(--ink)}
.spread{position:absolute;left:14px;width:760px;height:537px;display:flex;box-shadow:0 6px 18px rgba(0,0,0,.18)}
.spread--outside{top:40px}
.spread--inside{top:620px}
.panel{position:relative;width:380px;height:537px;overflow:hidden}
.panel--green{background:repeating-linear-gradient(90deg,var(--wood-green) 0 30px,var(--wood-green-line) 30px 31px)}
.panel--beige{background:repeating-linear-gradient(90deg,var(--wood-beige) 0 30px,var(--wood-beige-line) 30px 31px)}
.panel + .panel{border-left:1px solid rgba(0,0,0,.12)}

.tab{position:absolute;background:var(--white);border-radius:0 0 18px 18px;box-shadow:0 2px 4px rgba(0,0,0,.15)}
.tab::after{content:"";position:absolute;inset:5px;border:1.5px dashed var(--tab-dash);border-radius:0 0 14px 14px;border-top:none}
.tab--bottom{border-radius:18px 18px 0 0}
.tab--bottom::after{border-radius:14px 14px 0 0;border-top:1.5px dashed var(--tab-dash);border-bottom:none}
.brand{position:absolute;inset:0;display:flex;align-items:center;justify-content:center;gap:10px;font-family:"Crimson Pro",Georgia,serif;font-weight:700;font-size:28px;color:var(--logo-green)}
.brand-dot{width:30px;height:30px;border-radius:50%;background:var(--logo-green)}

/* back */
.back-headline{position:absolute;top:42px;left:0;right:0;text-align:center;font-family:"Boogaloo",cursive;font-size:32px;line-height:38px;color:var(--yellow);letter-spacing:1px;text-shadow:1px 2px 2px rgba(0,0,0,.25)}
.rule{position:absolute;left:50px;right:50px;height:1.5px;background:rgba(255,255,255,.85)}
.contact{position:absolute;top:268px;left:0;right:0;text-align:center;color:var(--white);font-size:15px;line-height:22px}
.contact strong{font-weight:700}
.back .tab{left:90px;bottom:0;width:200px;height:84px}
.back .brand{font-size:22px;gap:8px}
.back .brand-dot{width:24px;height:24px}

/* front */
.front .tab{right:22px;top:0;width:280px;height:84px}
.front-title{position:absolute;top:118px;left:0;right:0;text-align:center;font-family:"Boogaloo",cursive;font-size:31px;line-height:38px;color:var(--white);letter-spacing:1px;text-shadow:1px 2px 2px rgba(0,0,0,.25)}
.free-trial{position:absolute;top:196px;left:0;right:0;text-align:center;font-family:"Patua One",Georgia,serif;font-size:44px;color:var(--yellow);letter-spacing:2px;text-shadow:2px 3px 3px rgba(0,0,0,.3)}
.free-trial sup{font-size:20px;vertical-align:top}
.produce-photo{position:absolute;left:0;right:0;bottom:0;height:176px;border-top:5px solid #6b5a3e;background:linear-gradient(90deg,#5e8f2d 0%,#6a3e78 22%,#d8d2c4 36%,#7a9a3a 52%,#c8d85a 66%,#b8222a 84%,#d63a2e 100%)}

/* inside left */
.inside-tab{left:22px;right:22px;top:0;height:52px}
.inside-right .inside-tab{left:22px;right:22px}
.tab-title{position:absolute;inset:0;display:flex;align-items:center;justify-content:center;font-size:19px;color:var(--red)}
.sizes{position:absolute;top:72px;left:18px;right:18px;display:flex}
.size{flex:1;text-align:center;color:var(--white);position:relative}
.size + .size{border-left:2px dotted rgba(255,255,255,.8)}
.size svg{display:block;margin:36px auto 8px}
.size-name{font-weight:700;font-size:17px;letter-spacing:1px;text-shadow:0 1px 2px rgba(0,0,0,.25)}
.size-price{margin-top:18px;font-weight:700;font-size:24px;color:var(--red)}
.size-contents{margin-top:18px;font-size:17px;line-height:21px;text-shadow:0 1px 2px rgba(0,0,0,.2)}
.size-small svg{margin-top:50px}
.trial-ribbon{position:absolute;top:70px;left:12px;background:var(--red);color:var(--white);font-family:"Patua One",Georgia,serif;font-size:9px;line-height:11px;text-align:center;padding:4px 7px;transform:rotate(-4deg);box-shadow:0 1px 2px rgba(0,0,0,.3)}
.veg-silhouettes{position:absolute;left:0;right:0;top:378px;height:70px;background:linear-gradient(180deg,rgba(255,255,255,.75),rgba(255,255,255,.9))}
.footnote{position:absolute;left:0;right:0;bottom:0;height:64px;background:var(--cream);text-align:center;color:var(--red);font-size:10.5px;line-height:13px;padding-top:12px}

/* inside right */
.products{position:absolute;top:66px;left:14px;right:14px;display:grid;grid-template-columns:repeat(4,1fr);row-gap:10px}
.product{text-align:center;color:var(--white);font-size:11px;line-height:12px;height:105px;text-shadow:0 1px 2px rgba(0,0,0,.3)}
.product-name{height:32px;display:flex;align-items:flex-end;justify-content:center;padding:0 4px}
.product-photo{width:56px;height:52px;margin:8px auto 0;border-radius:10px}
</style>
</head>
<body>

<section class="spread spread--outside">
  <div class="panel panel--green back">
    <h2 class="back-headline">FARM FRESH<br>FRUIT &amp; VEGETABLES<br>DIRECT TO<br>YOUR DOORSTEP!</h2>
    <div class="rule" style="top:252px"></div>
    <div class="contact">
      <strong>Dorans Greens 2012</strong><br>
      Nora Doran<br>
      BSc (Hons) Horticultural Crop Production<br>
      Company Number: 8034417<br>
      <strong>0800 555 0192</strong><br>
      <strong>www.doransgreens.co.uk</strong>
    </div>
    <div class="rule" style="top:412px"></div>
    <div class="tab tab--bottom"><div class="brand"><span class="brand-dot"></span>Dorans Greens</div></div>
  </div>

  <div class="panel panel--green front">
    <div class="tab"><div class="brand"><span class="brand-dot"></span>Dorans Greens</div></div>
    <h1 class="front-title">HOME DELIVERY<br>FRUIT &amp; VEGETABLE BOX</h1>
    <p class="free-trial">FREE TRIAL<sup>*</sup></p>
    <div class="produce-photo" role="img" aria-label="Photograph of fresh produce: lettuce, red cabbage, mushrooms, asparagus, pumpkins, grapes and apples"></div>
  </div>
</section>

<section class="spread spread--inside">
  <div class="panel panel--beige inside-left">
    <div class="tab inside-tab"><p class="tab-title">We deliver boxes of the following sizes:</p></div>
    <p class="trial-ribbon">ELIGABLE FOR<br>FREE TRIAL!</p>
    <div class="sizes">
      <div class="size size-small">
        <svg width="30" height="32" viewBox="0 0 40 44"><path d="M20 2 38 12 20 22 2 12Z" fill="#fff"/><path d="M2 14 19 24V42L2 32Z" fill="#fff"/><path d="M38 14 21 24V42L38 32Z" fill="#fff"/></svg>
        <p class="size-name">SMALL</p>
        <p class="size-price">£7.50</p>
        <p class="size-contents">Contains:<br>2 Fruit<br>3 Veg</p>
      </div>
      <div class="size">
        <svg width="42" height="46" viewBox="0 0 40 44"><path d="M20 2 38 12 20 22 2 12Z" fill="#fff"/><path d="M2 14 19 24V42L2 32Z" fill="#fff"/><path d="M38 14 21 24V42L38 32Z" fill="#fff"/></svg>
        <p class="size-name">MEDIUM</p>
        <p class="size-price">£13.00</p>
        <p class="size-contents">Contains:<br>2 Fruit<br>5 Veg</p>
      </div>
      <div class="size">
        <svg width="50" height="55" viewBox="0 0 40 44" style="margin-top:28px"><path d="M20 2 38 12 20 22 2 12Z" fill="#fff"/><path d="M2 14 19 24V42L2 32Z" fill="#fff"/><path d="M38 14 21 24V42L38 32Z" fill="#fff"/></svg>
        <p class="size-name">LARGE</p>
        <p class="size-price">£18.50</p>
        <p class="size-contents">Contains:<br>3 Fruit<br>7 Veg</p>
      </div>
    </div>
    <div class="veg-silhouettes" role="img" aria-label="Row of white fruit and vegetable silhouettes ending in a pumpkin"></div>
    <p class="footnote">*Free Trial Box Offer<br>(no commitment or obligation, £2 delivery charge applies, contents are 100% free)<br>Offer applies to small boxes only.</p>
  </div>

  <div class="panel panel--beige inside-right">
    <div class="tab inside-tab"><p class="tab-title">We also deliver:</p></div>
    <div class="products">
      <div class="product"><p class="product-name">Bread, Morning Goods &amp; Dairy</p><div class="product-photo" role="img" aria-label="Photo of bread and a milk bottle" style="background:linear-gradient(90deg,#c98a3c,#f2efe6)"></div></div>
      <div class="product"><p class="product-name">Fruit Juices &amp; Soups</p><div class="product-photo" role="img" aria-label="Photo of orange juice" style="background:linear-gradient(180deg,#f6a632,#e87a1c)"></div></div>
      <div class="product"><p class="product-name">Meat Boxes</p><div class="product-photo" role="img" aria-label="Photo of raw steaks" style="background:linear-gradient(135deg,#b23a44,#8a2230)"></div></div>
      <div class="product"><p class="product-name">Gourmet Sausages &amp; Pies</p><div class="product-photo" role="img" aria-label="Photo of sausages" style="background:linear-gradient(135deg,#e8a89a,#d8847a)"></div></div>
      <div class="product"><p class="product-name">Pies &amp; Savoury Crumbles</p><div class="product-photo" role="img" aria-label="Photo of savoury pastries" style="background:linear-gradient(135deg,#c7782e,#8a6a2a)"></div></div>
      <div class="product"><p class="product-name">Weekend Treats &amp; Snacks</p><div class="product-photo" role="img" aria-label="Photo of shortbread fingers" style="background:linear-gradient(135deg,#efd9a4,#d9bc7c)"></div></div>
      <div class="product"><p class="product-name">Desserts &amp; Sweet Crumbles</p><div class="product-photo" role="img" aria-label="Photo of a dessert" style="background:linear-gradient(135deg,#8a5a32,#d8c0a0)"></div></div>
      <div class="product"><p class="product-name">Artisan Pasta</p><div class="product-photo" role="img" aria-label="Photo of pasta" style="background:linear-gradient(135deg,#f4e6a8,#e6cf78)"></div></div>
      <div class="product"><p class="product-name">Jams, Curds &amp; Honey</p><div class="product-photo" role="img" aria-label="Photo of a jar of jam" style="background:linear-gradient(135deg,#d8283a,#9a1424)"></div></div>
      <div class="product"><p class="product-name">Fish</p><div class="product-photo" role="img" aria-label="Photo of salmon fillets" style="background:linear-gradient(135deg,#f07a5a,#e4603e)"></div></div>
      <div class="product"><p class="product-name">Vegetarian &amp; Gluten Free Foods</p><div class="product-photo" role="img" aria-label="Photo of dark rye bread" style="background:linear-gradient(135deg,#5a3a24,#3a2414)"></div></div>
      <div class="product"><p class="product-name">Risotto &amp; Couscous</p><div class="product-photo" role="img" aria-label="Photo of a plate of risotto" style="background:linear-gradient(135deg,#f6f2e6,#d8cfae)"></div></div>
      <div class="product"><p class="product-name">Tea, Coffee, Biscuits &amp; Cereals</p><div class="product-photo" role="img" aria-label="Photo of a cup of tea" style="background:linear-gradient(180deg,#c9a48a,#f2f0ec)"></div></div>
      <div class="product"><p class="product-name">Cooking Sauces &amp; Condiments</p><div class="product-photo" role="img" aria-label="Photo of a bowl of sauce" style="background:linear-gradient(180deg,#7a1a22,#f0ece6)"></div></div>
      <div class="product"><p class="product-name">Herbs &amp; More Fresh Produce</p><div class="product-photo" role="img" aria-label="Photo of fresh herbs" style="background:linear-gradient(135deg,#5e9a3a,#2e6a1e)"></div></div>
      <div class="product"><p class="product-name">For the Store Cupboard</p><div class="product-photo" role="img" aria-label="Photo of a jar of olives" style="background:linear-gradient(135deg,#a8b03a,#6a7a1e)"></div></div>
    </div>
  </div>
</section>

</body>
</html>
```